Nimble Bench Gigs website

Our business is a freelance marketplace for IT and Digital contractors. It will provide a way for companies to take advantage of specialist talent for small periods of time and engage with them on a flexible basis. Logo should be something that shows Knowledge, Agility, Unlocking. Modern, simple, genius.We are looking for a site that conveys three things:- To have great technology you need great software, great hardware and great people. No one argues with that. To spend your dollars wisely and to focus on your core business, you have Cloud software and Cloud Hardware. Are any of your people in the cloud?- 5 specialists for the cost of one generalist- Cloud, agile and communication are converging to make the business case for remote specialists irresistible, we can get you the people you need to get your projects done, today.

Target Market(s)

Businesses, Tech professionals, Sales People, Recruiters

Industry/Entity Type

Information Technology

Logo Text

NimbleBenchGigs or NBG

Coding

Coded - Design and coding required

Number of Pages Required

5+ page

Font styles to use
Sans Serif

Colors

Designer to choose colors to be used in the design.

Requirements
Must have
• A beautiful landing page with a technical feel to it
• a nice slick graphic for the How it works...
• A look and feel that is consistent throughout
• Some moving text
Should not have
• ugly anything

```html
<!DOCTYPE html>
<html lang="en">
<head>
<meta charset="utf-8">
<title>Nimble Bench Gigs</title>
<link href="https://fonts.googleapis.com/css2?family=Poppins:wght@500;600;700&family=Open+Sans:wght@400;600;700&family=Roboto:wght@400;500;700&display=swap" rel="stylesheet">
<style>
:root{
  --teal:#139fb3;
  --teal-band:#18a3b6;
  --yellow:#dede00;
  --orange:#f25a24;
  --ink:#3a3a3a;
  --dark:#2f2f2f;
  --pale:#f3f2f1;
  --grey-num:#c9c9c9;
  --white:#ffffff;
}
*{box-sizing:border-box;margin:0;padding:0}
html,body{width:717px;height:1200px;overflow:hidden;background:var(--white)}
body{font-family:"Open Sans",sans-serif;color:var(--ink)}
.page{position:relative;width:717px;height:1200px;overflow:hidden}
.abs{position:absolute}

/* hero */
.hero{position:absolute;left:0;top:0;width:717px;height:392px;overflow:hidden}
.hero-photo{position:absolute;inset:0;background:linear-gradient(100deg,#5a5d63 0%,#6b6e73 35%,#54565b 60%,#3d4048 100%)}
.hero-shade{position:absolute;inset:0;background:rgba(40,42,50,.35)}
.nav-burger{left:79px;top:17px;width:12px;height:10px}
.nav-link{top:17px;font-family:"Poppins",sans-serif;font-weight:600;font-size:8px;color:var(--white);letter-spacing:.2px}
.nav-btn{top:14px;height:17px;font-family:"Open Sans",sans-serif;font-weight:700;font-size:8px;color:var(--white);display:flex;align-items:center;justify-content:center;border:1px solid var(--white)}
.nav-btn.start{background:var(--orange);border-color:var(--orange)}
.brand-mark{left:0;width:717px;top:100px;text-align:center;font-family:"Poppins",sans-serif;font-weight:700;font-size:22px;color:var(--yellow);letter-spacing:1px}
.hero-title{left:0;width:717px;top:158px;text-align:center;font-family:"Poppins",sans-serif;font-weight:700;font-size:22px;color:var(--white)}
.hero-ask{left:0;width:717px;top:226px;text-align:center;font-family:"Open Sans",sans-serif;font-weight:600;font-size:12px;color:var(--white)}
.role{top:263px;width:103px;height:85px;border:2px solid var(--teal);display:flex;flex-direction:column;align-items:center;justify-content:center;gap:8px;font-weight:600;font-size:10px;color:var(--white);letter-spacing:.3px}
.role.active{background:var(--teal)}
.scroll-cue{left:345px;top:380px;width:27px;height:27px;border-radius:50%;background:var(--white)}

/* how it works */
.section-title{left:0;width:717px;top:422px;text-align:center;font-family:"Poppins",sans-serif;font-weight:700;font-size:24px;color:var(--ink)}
.title-rule{left:345px;top:460px;width:26px;height:2px;background:var(--yellow)}
.step-title{font-family:"Poppins",sans-serif;font-weight:500;font-size:11px;color:#1f1f1f}
.step-text{font-size:8px;line-height:10.5px;color:#444}
.step-num{font-family:"Open Sans",sans-serif;font-weight:400;font-size:34px;color:var(--grey-num)}

/* stats */
.stats{left:0;top:867px;width:717px;height:132px;background:var(--teal-band)}
.stat{position:absolute;top:0;width:130px;text-align:center;color:var(--white)}
.stat svg{position:absolute;left:50%;top:20px;transform:translateX(-50%)}
.stat-num{position:absolute;top:72px;width:100%;font-family:"Poppins",sans-serif;font-weight:700;font-size:15px}
.stat-label{position:absolute;top:97px;width:100%;font-size:8.5px;line-height:12px;letter-spacing:.2px}

/* footer */
.footer{left:0;top:999px;width:717px;height:201px;background:var(--dark);color:var(--white);font-family:"Roboto",sans-serif}
.footer-brand{position:absolute;left:95px;top:90px;font-family:"Open Sans",sans-serif;font-weight:700;font-size:15px;color:var(--yellow)}
.foot-head{position:absolute;top:28px;font-weight:700;font-size:7px;letter-spacing:.3px}
.foot-text{position:absolute;font-size:6.5px;line-height:9px}
.foot-menu{position:absolute;left:449px;top:51px;font-size:6.5px;line-height:12px;list-style:none}
.social{position:absolute;left:569px;display:flex;align-items:center;gap:7px;font-size:6.5px}
.social i{display:block;width:16px;height:16px;border-radius:50%}
.foot-rule{position:absolute;left:295px;top:141px;width:330px;height:1px;background:#4a4a4a}
.copyright{position:absolute;left:0;width:926px;top:167px;text-align:center;font-size:6.5px}
.foot-bar{position:absolute;left:0;bottom:0;width:717px;height:3px;background:var(--yellow)}
</style>
</head>
<body>
<div class="page">

  <header class="hero">
    <div class="hero-photo" role="img" aria-label="Photo of a smiling professional working on a laptop in a bright office"></div>
    <div class="hero-shade"></div>

    <svg class="abs nav-burger" viewBox="0 0 12 10"><rect y="0" width="12" height="2" fill="#fff"/><rect y="4" width="12" height="2" fill="#fff"/><rect y="8" width="12" height="2" fill="#fff"/></svg>
    <div class="abs nav-link" style="left:105px">COMPANY</div>
    <div class="abs nav-link" style="left:164px">HOW IT WORKS</div>
    <div class="abs nav-btn" style="left:487px;width:40px">LOGIN</div>
    <div class="abs nav-btn" style="left:539px;width:44px">SIGNUP</div>
    <div class="abs nav-btn start" style="left:595px;width:44px">START</div>

    <div class="abs brand-mark">NBG</div>
    <h1 class="abs hero-title">NIMBLE BENCH GIGS</h1>
    <p class="abs hero-ask">Do you want to be a...</p>

    <div class="abs role" style="left:183px">
      <svg width="26" height="26" viewBox="0 0 26 26"><rect x="2" y="4" width="20" height="20" rx="2" fill="none" stroke="#fff" stroke-width="3"/><path d="M9 17 L21 4 L24 7 L12 19 L8 20 Z" fill="#fff"/></svg>
      <span>GIGGER</span>
    </div>
    <div class="abs role active" style="left:307px">
      <svg width="26" height="28" viewBox="0 0 26 28"><circle cx="13" cy="8" r="6" fill="#fff"/><path d="M1 28 C1 19 6 16 13 16 C20 16 25 19 25 28 Z" fill="#fff"/><path d="M12 17 L14 17 L14 28 L12 28 Z" fill="#139fb3"/></svg>
      <span>CUSTOMER</span>
    </div>
    <div class="abs role" style="left:431px">
      <svg width="34" height="30" viewBox="0 0 34 30" fill="none" stroke="#fff" stroke-width="2"><circle cx="17" cy="15" r="7"/><circle cx="17" cy="13" r="2.5" fill="#fff"/><path d="M17 8 V3 M10 15 H4 M24 15 H30 M12 20 L7 26 M22 20 L27 26"/><circle cx="17" cy="3" r="2" fill="#fff"/><circle cx="3" cy="15" r="2" fill="#fff"/><circle cx="31" cy="15" r="2" fill="#fff"/><circle cx="6" cy="27" r="2" fill="#fff"/><circle cx="28" cy="27" r="2" fill="#fff"/></svg>
      <span>AFFILIATE</span>
    </div>

    <div class="abs scroll-cue"><svg width="27" height="14" viewBox="0 0 27 14"><path d="M9 6 L13.5 10 L18 6" fill="none" stroke="#3a3a3a" stroke-width="1.4"/></svg></div>
  </header>

  <section class="how">
    <h2 class="abs section-title">How it works</h2>
    <div class="abs title-rule"></div>

    <div class="abs step-title" style="left:0;width:717px;text-align:center;top:486px">Specialists</div>
    <p class="abs step-text" style="left:255px;width:207px;text-align:center;top:507px">Lorem ipsum dolor sit amet consectetur adi piscing elit, sed do eiu smod tempor inc ididunt ut labore et dolore magna aliqua. Ut enim ad minim.</p>

    <svg class="abs" style="left:0;top:540px" width="717" height="300" viewBox="0 540 717 300">
      <circle cx="354" cy="695" r="79" fill="#f3f2f1"/>
      <path d="M302 604 Q252 640 248 692" fill="none" stroke="#55606c" stroke-width="2" stroke-dasharray="1.5 3"/>
      <path d="M243 693 L249 698 L254 693" fill="none" stroke="#55606c" stroke-width="2"/>
      <path d="M406 603 Q456 630 460 700" fill="none" stroke="#55606c" stroke-width="2" stroke-dasharray="1.5 3"/>
      <path d="M409 597 L403 603 L406 609" fill="none" stroke="#55606c" stroke-width="2"/>
      <path d="M296 786 Q350 812 406 792" fill="none" stroke="#139fb3" stroke-width="2" stroke-dasharray="1.5 3"/>
      <path d="M403 787 L409 791 L407 798" fill="none" stroke="#139fb3" stroke-width="2"/>
      <circle cx="355" cy="594" r="44" fill="#139fb3"/>
      <circle cx="355" cy="582" r="10" fill="#fff"/>
      <path d="M335 612 C335 598 343 594 355 594 C367 594 375 598 375 612 Z" fill="#fff"/>
      <rect x="354" y="596" width="2" height="16" fill="#139fb3"/>
      <circle cx="266" cy="746" r="44" fill="#3a3a3a"/>
      <rect x="247" y="735" width="38" height="28" rx="3" fill="#fff"/>
      <path d="M259 735 V730 H273 V735" fill="none" stroke="#fff" stroke-width="2.5"/>
      <path d="M247 746 L266 752 L285 746" fill="none" stroke="#3a3a3a" stroke-width="1.2"/>
      <rect x="263" y="749" width="6" height="6" fill="none" stroke="#3a3a3a" stroke-width="1.2"/>
      <circle cx="444" cy="746" r="44" fill="#dede00"/>
      <g fill="none" stroke="#fff" stroke-width="2.5">
        <circle cx="444" cy="746" r="11"/>
        <path d="M444 735 V727 M433 746 H424 M455 746 H464 M436 754 L430 762 M452 754 L458 762"/>
      </g>
      <g fill="#fff"><circle cx="444" cy="743" r="4"/><circle cx="444" cy="725" r="3"/><circle cx="422" cy="746" r="3"/><circle cx="466" cy="746" r="3"/><circle cx="429" cy="764" r="3"/><circle cx="459" cy="764" r="3"/></g>
      <text x="354" y="703" text-anchor="middle" font-family="Poppins, sans-serif" font-weight="700" font-size="22" fill="#139fb3">NBG</text>
    </svg>

    <div class="abs step-num" style="left:214px;top:602px">01</div>
    <div class="abs step-num" style="left:459px;top:617px">03</div>
    <div class="abs step-num" style="left:338px;top:808px">02</div>

    <div class="abs step-title" style="left:80px;width:124px;text-align:right;top:703px">Business</div>
    <p class="abs step-text" style="left:80px;width:125px;text-align:right;top:722px">Lorem ipsum dolor sit amet, consectetur adi piscing elit, sed do eiu smod tempor inc ididu nt ut labore et dolore magna aliqua. Ut enim ad minim veniam, quis nostrud</p>
    <div class="abs step-title" style="left:504px;top:703px">Affiliate</div>
    <p class="abs step-text" style="left:504px;width:125px;top:722px">Lorem ipsum dolor sit amet, consectetur adi piscing elit, sed do eiu smod tempor inc ididu nt ut labore et dolore magna aliqua. Ut enim ad minim veniam, quis nostrud</p>
  </section>

  <section class="abs stats">
    <div class="stat" style="left:53px">
      <svg width="30" height="40" viewBox="0 0 30 40" fill="#fff"><circle cx="7" cy="4" r="3.5"/><path d="M3 9 H9 V22 H20 V26 H14 V38 H11 V26 H3 Z"/><path d="M19 12 L28 10 L24 22 H21 Z" opacity=".9"/><rect x="8" y="38" width="10" height="2"/></svg>
      <div class="stat-num">100%</div>
      <div class="stat-label">TRUST<br>FREELANCING</div>
    </div>
    <div class="stat" style="left:169px">
      <svg width="28" height="28" viewBox="0 0 26 26"><rect x="2" y="4" width="20" height="20" rx="2" fill="none" stroke="#fff" stroke-width="3"/><path d="M9 17 L21 4 L24 7 L12 19 L8 20 Z" fill="#fff"/></svg>
      <div class="stat-num">2158</div>
      <div class="stat-label">JOBS<br>POSTED</div>
    </div>
    <div class="stat" style="left:293px">
      <svg width="30" height="30" viewBox="0 0 30 30" fill="#fff"><rect x="1" y="13" width="6" height="15" rx="1"/><path d="M9 13 L15 2 C18 2 18 5 17 9 H27 C29 9 30 11 29 13 L27 26 C26 28 25 28 23 28 H9 Z"/></svg>
      <div class="stat-num">6521</div>
      <div class="stat-label">CUSTOMER<br>SATISFACTION</div>
    </div>
    <div class="stat" style="left:421px">
      <svg width="34" height="30" viewBox="0 0 34 30"><rect x="1" y="7" width="32" height="22" rx="3" fill="#fff"/><path d="M11 7 V2 H23 V7" fill="none" stroke="#fff" stroke-width="2.5"/><path d="M1 16 L17 20 L33 16" fill="none" stroke="#18a3b6" stroke-width="1.2"/><rect x="14" y="17" width="6" height="5" fill="none" stroke="#18a3b6" stroke-width="1.2"/></svg>
      <div class="stat-num">5+</div>
      <div class="stat-label">YEARS<br>EXPERIENCE</div>
    </div>
    <div class="stat" style="left:547px">
      <svg width="30" height="30" viewBox="0 0 30 30" fill="none" stroke="#fff" stroke-width="2"><circle cx="15" cy="15" r="13"/><ellipse cx="15" cy="15" rx="6" ry="13"/><path d="M2 15 H28 M4 8 H26 M4 22 H26 M15 2 V28"/></svg>
      <div class="stat-num">15</div>
      <div class="stat-label">GLOBAL<br>LOCATIONS</div>
    </div>
  </section>

  <footer class="abs footer">
    <div class="footer-brand">Nimble Bench Gigs</div>

    <div class="foot-head" style="left:298px">CONTACT US</div>
    <svg class="abs" style="left:297px;top:53px" width="6" height="8" viewBox="0 0 6 8"><path d="M3 0 C5 0 6 1.4 6 3 C6 5 3 8 3 8 C3 8 0 5 0 3 C0 1.4 1 0 3 0 Z" fill="#fff"/><circle cx="3" cy="3" r="1.1" fill="#2f2f2f"/></svg>
    <div class="foot-text" style="left:310px;top:52px">2750 Larkspur Lane<br>Maple Ridge, CA 90210</div>
    <svg class="abs" style="left:297px;top:82px" width="7" height="7" viewBox="0 0 7 7"><path d="M1 0 L2.6 1.8 L1.8 2.8 C2.4 4 3 4.6 4.2 5.2 L5.2 4.4 L7 6 L6 7 C3 7 0 4 0 1 Z" fill="#fff"/></svg>
    <div class="foot-text" style="left:310px;top:81px">555.014.2368</div>
    <svg class="abs" style="left:297px;top:103px" width="8" height="6" viewBox="0 0 8 6"><rect width="8" height="6" fill="#fff"/><path d="M0 0 L4 3.5 L8 0" fill="none" stroke="#2f2f2f" stroke-width=".9"/></svg>
    <div class="foot-text" style="left:312px;top:102px">hello@nimblebenchgigs.com</div>

    <div class="foot-head" style="left:449px">MENU</div>
    <ul class="foot-menu"><li>HOME</li><li>ABOUT US</li><li>HOW IT WORKS</li><li>LOGIN</li><li>SIGNUP</li></ul>

    <div class="foot-head" style="left:568px">CONNECT WITH US</div>
    <div class="social" style="top:50px"><i style="background:#3b5998"></i>Circlepage</div>
    <div class="social" style="top:74px"><i style="background:#1da1f2"></i>Chirpline</div>
    <div class="social" style="top:97px"><i style="background:#1b2a5c"></i>Workweb</div>

    <div class="foot-rule"></div>
    <div class="copyright">Copyright © &nbsp;2019 All Rights Reserved</div>
    <div class="foot-bar"></div>
  </footer>

</div>
</body>
</html>
```